Sunmeadow Home Care Business Card

We are a home care company customizing in personal care services. Our personal care service is different because our mission is to provide the most effective care while enhancing quality of life. We strive to make everyday our client's best day. I would like a very classic and/or retro feel. I don't like clip art.

Target Market(s)

doctor's offices; potential clients

Industry/Entity Type

Business

Contact Information for Business Card

jdalton@sunmeadowhc.example(919) 480-15904000 Blue Ridge Road, Suite 101Raleigh, NC 27612www.SunmeadowHC.example

Requirements
Must have
• classic and/or retro feel. Very caring.
Should not have
• Clip art

```html
<!DOCTYPE html>
<html lang="en">
<head>
<meta charset="utf-8">
<title>Sunmeadow Home Care – Business Card</title>
<link rel="stylesheet" href="https://fonts.googleapis.com/css2?family=Handlee&display=swap">
<style>
  :root {
    --sky: #0f9ad3;
    --leaf: #8dc043;
    --paper: #ffffff;
    --ink: #2b2b2b;
    --backdrop: #eeeeee;
  }
  * { margin: 0; padding: 0; box-sizing: border-box; }
  html, body { width: 1200px; height: 963px; overflow: hidden; }
  body {
    background: var(--backdrop);
    position: relative;
    font-family: "Handlee", cursive;
  }
  .card {
    position: absolute;
    width: 560px;
    height: 320px;
    background: var(--paper);
    box-shadow: 0 6px 18px rgba(0,0,0,0.12);
    overflow: hidden;
  }
  .card-front { left: 60px; top: 130px; }
  .card-back  { left: 580px; top: 500px; }
  .card-shapes { position: absolute; inset: 0; width: 100%; height: 100%; }
  .shape-sky  { fill: var(--sky); }
  .shape-leaf { fill: var(--leaf); }

  .wordmark {
    position: absolute;
    color: var(--sky);
    font-weight: 400;
    line-height: 1.05;
    white-space: nowrap;
  }
  .card-front .wordmark { left: 170px; top: 128px; font-size: 30px; }
  .card-back .wordmark  { right: 40px; top: 52px; font-size: 28px; text-align: right; }

  .contact-list {
    position: absolute;
    left: 250px;
    top: 124px;
    list-style: none;
    color: var(--ink);
    font-size: 15px;
    line-height: 1.35;
  }
  .contact-list li {
    display: flex;
    align-items: flex-start;
    gap: 8px;
    margin-bottom: 5px;
  }
  .contact-icon { flex: none; width: 16px; height: 16px; margin-top: 2px; }
  .contact-icon circle.badge { fill: var(--leaf); }
  .contact-icon .glyph { fill: none; stroke: var(--paper); stroke-width: 1.3; stroke-linecap: round; stroke-linejoin: round; }
</style>
</head>
<body>

  <section class="card card-front" aria-label="Card front">
    <svg class="card-shapes" viewBox="0 0 560 320" aria-hidden="true">
      <polygon class="shape-sky" points="0,0 300,0 0,200"/>
      <polygon class="shape-leaf" points="560,110 560,320 260,320"/>
    </svg>
    <p class="wordmark">Sunmeadow<br>Home Care, Inc.</p>
  </section>

  <section class="card card-back" aria-label="Card back">
    <svg class="card-shapes" viewBox="0 0 560 320" aria-hidden="true">
      <polygon class="shape-sky" points="390,0 560,0 560,44"/>
      <polygon class="shape-leaf" points="0,280 300,262 0,320"/>
    </svg>
    <p class="wordmark">Sunmeadow<br>Home Care, Inc.</p>
    <ul class="contact-list">
      <li>
        <svg class="contact-icon" viewBox="0 0 16 16" aria-hidden="true">
          <circle class="badge" cx="8" cy="8" r="8"/>
          <path class="glyph" d="M8 12.5 C5.5 9.5 5 8.4 5 7 a3 3 0 0 1 6 0 c0 1.4 -0.5 2.5 -3 5.5z"/>
        </svg>
        <span>2700 Copper Finch Lane,<br>Suite 101 Fairbrook, NC 27000</span>
      </li>
      <li>
        <svg class="contact-icon" viewBox="0 0 16 16" aria-hidden="true">
          <circle class="badge" cx="8" cy="8" r="8"/>
          <path class="glyph" d="M5.5 4.5 l1.5 0 l0.8 2 l-1 0.8 a5 5 0 0 0 2 2 l0.8 -1 l2 0.8 l0 1.5 a1 1 0 0 1 -1 1 a7 7 0 0 1 -6 -6 a1 1 0 0 1 1 -1z"/>
        </svg>
        <span>(555) 302-7741</span>
      </li>
      <li>
        <svg class="contact-icon" viewBox="0 0 16 16" aria-hidden="true">
          <circle class="badge" cx="8" cy="8" r="8"/>
          <path class="glyph" d="M4 5.5 h8 v5 h-8z M4 5.5 l4 3 l4 -3"/>
        </svg>
        <span>jdalton@sunmeadowhc.example</span>
      </li>
      <li>
        <svg class="contact-icon" viewBox="0 0 16 16" aria-hidden="true">
          <circle class="badge" cx="8" cy="8" r="8"/>
          <circle class="glyph" cx="8" cy="8" r="4.2"/>
          <path class="glyph" d="M3.8 8 h8.4 M8 3.8 c-2 2.5 -2 5.9 0 8.4 M8 3.8 c2 2.5 2 5.9 0 8.4"/>
        </svg>
        <span>www.SunmeadowHC.example</span>
      </li>
    </ul>
  </section>

</body>
</html>
```